Postcard For neighbors near worksite

We are a residential interior and exterior painting company. I will be sending post cards out in neighborhoods that we will be currently working in. Basically giving the neighbors a "Neighborhood Notice" that we are in the area and would like to give a Free Estimate to anyone in that neighborhood. I will attach a file of another companies idea that I like. Also, I attached my Logo. Brightcoat Painting & More

Target Market(s)

Neighbors near where we are working

Industry/Entity Type

It Company

Requirements
Must have
• Website: Brightcoatpaint.example
• Number: 555.204.6617

```html
<!DOCTYPE html>
<html lang="en">
<head>
<meta charset="utf-8">
<title>Brightcoat Painting &amp; More – Neighborhood Postcard</title>
<link rel="stylesheet" href="https://fonts.googleapis.com/css2?family=Jost:wght@500;700;800&display=swap">
<style>
  :root{
    --brand-red:#f0130f;
    --slate-grey:#7a8582;
    --ink:#141414;
    --paper:#ffffff;
  }
  *{margin:0;padding:0;box-sizing:border-box}
  html,body{width:1200px;height:669px;overflow:hidden;background:var(--paper)}
  .postcard{position:relative;width:1200px;height:669px;overflow:hidden;background:var(--paper);font-family:"Jost",sans-serif}
  .backdrop{position:absolute;inset:0;width:1200px;height:669px}
  .intro{position:absolute;left:64px;top:56px;width:390px;color:var(--paper);font-weight:700;font-size:15px;line-height:1.2}
  .intro p + p{margin-top:18px}
  .testimonial{position:absolute;left:64px;top:321px;width:350px;color:var(--ink);font-weight:700;font-size:15.5px;line-height:1.2}
  .testimonial cite{display:block;font-style:normal}
  .call-to-action{position:absolute;left:64px;top:477px;font-weight:800;line-height:1.05;letter-spacing:.3px}
  .call-to-action .phone{color:var(--slate-grey);font-size:36px}
  .call-to-action .offer{color:var(--brand-red);font-size:35px}
  .brand{position:absolute;left:437px;top:190px;display:flex;flex-direction:column;align-items:flex-start}
  .brand-square{width:140px;height:140px;background:var(--brand-red)}
  .brand-name{margin-top:22px;color:var(--ink);font-weight:500;font-size:31px;white-space:nowrap}
  .footer-band{position:absolute;left:0;bottom:0;width:1200px;height:84px;background:var(--brand-red);display:flex;align-items:center;padding-left:116px}
  .footer-band p{color:var(--paper);font-weight:700;font-size:39px;letter-spacing:.2px}
</style>
</head>
<body>
<main class="postcard">
  <svg class="backdrop" viewBox="0 0 1400 780" preserveAspectRatio="none" aria-hidden="true">
    <path d="M0 0 H680 C720 80 742 200 736 300 H0 Z" fill="var(--slate-grey)"/>
    <rect x="0" y="316" width="570" height="34" fill="var(--brand-red)"/>
    <path d="M705 -10 C765 130 705 300 714 430 C724 545 780 640 890 700" fill="none" stroke="var(--brand-red)" stroke-width="19"/>
  </svg>

  <section class="intro">
    <p>A home isn’t just where you live, it’s what you’ve worked for.</p>
    <p>You want your investment to be well protected with a quality paint job. We want you to be 100% satisfied.<br>Our courtesy, attention to detail, and desire to make a difference is what our customers talk about most.</p>
  </section>

  <div class="brand">
    <span class="brand-square"></span>
    <span class="brand-name">Brightcoat Painting &amp; More</span>
  </div>

  <blockquote class="testimonial">
    “The entire Brightcoat staff was very professional…from the office staff to the painting crew. The quality of the work was absolutely fantastic! We are happy to recommend them.”
    <cite>Dana R.</cite>
  </blockquote>

  <div class="call-to-action">
    <p class="phone">CALL: 555-204-6617</p>
    <p class="offer">FOR A FREE ESTIMATE</p>
  </div>

  <footer class="footer-band">
    <p>Visit brightcoatpaint.example for more information</p>
  </footer>
</main>
</body>
</html>
```